Back Pain

Need a flyer similar to the attached draft. This is to be handed out to prospective patients. Note that Artwell Studio has already designed the logo. If you need a copy please contact me

```html
<!DOCTYPE html>
<html lang="en">
<head>
<meta charset="utf-8">
<title>Tech Neck Flyer</title>
<link href="https://fonts.googleapis.com/css2?family=Barlow+Condensed:wght@400;500;600;700&family=Barlow+Semi+Condensed:wght@500;600&family=Montserrat:wght@600&display=swap" rel="stylesheet">
<style>
  :root{
    --navy:#232f3a;
    --green:#8cc63f;
    --blue:#1473bf;
    --sky:#27a9e1;
    --ink:#1f2a33;
    --pale:#eef5fc;
    --white:#ffffff;
    --red:#e8263c;
    --stage:#e2e2e2;
  }
  *{box-sizing:border-box;margin:0;padding:0}
  html,body{width:1200px;height:1200px;overflow:hidden;background:var(--stage)}
  body{font-family:"Barlow Condensed",sans-serif;color:var(--ink)}
  .flyer{position:absolute;left:218px;top:64px;width:763px;height:1071px;background:var(--white);overflow:hidden}
  .abs{position:absolute}
  .header{left:0;top:0;width:763px;height:177px;background:var(--navy)}
  .band-green{left:0;width:763px;background:var(--green)}
  .brand{left:78px;top:36px;width:200px;text-align:center}
  .brand-mark{width:70px;height:70px;border-radius:50%;background:var(--green);margin:0 auto 12px}
  .brand-name{font-family:"Montserrat",sans-serif;font-weight:600;font-size:15px;color:var(--sky);letter-spacing:-.3px;line-height:1}
  .brand-sub{font-family:"Montserrat",sans-serif;font-weight:600;font-size:7.5px;color:var(--sky);letter-spacing:1.6px;margin-top:4px}
  .title{left:359px;top:62px;font-weight:700;font-size:60px;line-height:1;color:var(--white);white-space:nowrap}
  .title span{color:var(--green)}
  .intro{left:49px;top:227px;font-family:"Barlow Semi Condensed",sans-serif;font-size:20.5px;line-height:30px;font-weight:500;white-space:nowrap}
  .intro strong{color:var(--green);font-weight:600}
  .chart-lead{left:49px;top:364px;font-size:21px;line-height:30px;font-weight:500}
  .chart-lead b{font-weight:700}
  .bar{background:var(--blue);color:var(--white);font-weight:600;font-size:30px;text-align:center;line-height:1}
  .tick{font-weight:700;font-size:32px;top:607px;line-height:1}
  .axis-x{left:60px;top:641px;font-weight:600;font-size:19px}
  .axis-y{left:212px;top:494px;width:200px;font-weight:600;font-size:15px;transform:rotate(-90deg);text-align:center}
  .head-art{left:57px;top:463px;width:70px;height:86px;border-radius:40px 30px 10px 30px;background:var(--navy)}
  .axis-line{left:52px;top:466px;width:1.5px;height:94px;background:var(--ink)}
  .figure-art{left:405px;top:219px;width:120px;height:469px;border-radius:50px 50px 0 0;background:linear-gradient(180deg,#f6c9a6 0%,#2f5f5a 30%,#2f5f5a 55%,#0f2a3a 100%)}
  .symptom{font-weight:700;font-size:28px;line-height:29px;color:var(--ink);white-space:nowrap}
  .lower{left:0;top:688px;width:763px;height:205px;background:var(--pale)}
  .stat{left:40px;top:800px;width:228px;text-align:center;line-height:1}
  .stat-a{font-weight:600;font-size:19px}
  .stat-b{font-weight:700;font-size:31px;margin:6px 0 5px}
  .stat-c{font-weight:600;font-size:19.5px;letter-spacing:.3px}
  .divider{left:305px;top:705px;width:1px;height:174px;background:#9aa3ab}
  .care{left:318px;top:708px;width:400px;text-align:center;font-weight:500;color:var(--ink)}
  .care p{line-height:33px;font-size:30px}
  .care .sm{font-size:25px}
  .care b{color:var(--blue);font-weight:600}
  .footer{left:0;top:900px;width:763px;height:171px;background:var(--navy)}
  .portrait{left:36px;top:917px;width:128px;height:128px;border-radius:50%;border:6px solid var(--white);background:radial-gradient(circle at 50% 45%,#d9b9a3 0%,#cfd6dc 60%,#eef1f3 100%)}
  .doc-name{left:177px;top:930px;font-size:30px;font-weight:500;color:var(--sky);line-height:1}
  .doc-addr{left:177px;top:966px;font-size:22px;font-weight:500;color:var(--white);line-height:1}
  .book{left:177px;top:997px;font-size:29px;font-weight:600;color:var(--white);line-height:1;display:flex;align-items:center;gap:10px}
  .phone-icon{width:28px;height:28px}
  .offer{left:502px;top:920px;width:222px;height:123px;border-radius:12px;background:var(--blue);color:var(--white);text-align:center}
  .offer-top{display:flex;align-items:center;justify-content:center;gap:6px;margin-top:8px;line-height:1}
  .offer-pct{font-weight:700;font-size:50px}
  .offer-off{font-weight:600;font-size:15px;line-height:16px;text-align:left}
  .offer-off span{font-size:20px}
  .offer-head{font-weight:700;font-size:22px;line-height:22px;text-align:left}
  .offer-rule{display:flex;align-items:center;gap:8px;justify-content:center;font-size:15px;margin-top:4px}
  .offer-rule i{display:block;width:28px;height:1px;background:var(--white)}
  .offer-url{font-weight:600;font-size:15px;margin-top:2px}
  .offer-note{font-size:15px;margin-top:1px}
  .offer-note b{font-weight:700}
</style>
</head>
<body>
<div class="flyer">
  <div class="abs header"></div>
  <div class="abs band-green" style="top:177px;height:14px"></div>

  <div class="abs brand">
    <div class="brand-mark"></div>
    <div class="brand-name">SPINE EASE CLINIC</div>
    <div class="brand-sub">DR SAM HARLOW - CHIROPRACTOR</div>
  </div>
  <h1 class="abs title">GOT <span>TECH NECK ?</span></h1>

  <p class="abs intro"><strong>Tech Neck</strong> is the act of stressing<br>muscles while using phones, tablets,<br>and computers, resulting in neck and<br>shoulder pain, stiffness, and soreness.</p>

  <div class="abs chart-lead">AS THE HEAD TILTS FORWARD.<br><b>MORE FORCE IS PLACED<br>ON THE SPINE</b></div>

  <div class="abs axis-line"></div>
  <div class="abs head-art" role="img" aria-label="Silhouette of a head tilting forward"></div>
  <div class="abs bar" style="left:52px;top:570px;width:35px;height:28px;line-height:28px">12</div>
  <div class="abs bar" style="left:106px;top:517px;width:36px;height:81px;padding-top:30px">27</div>
  <div class="abs bar" style="left:158px;top:473px;width:35px;height:125px;padding-top:50px">40</div>
  <div class="abs bar" style="left:211px;top:445px;width:36px;height:153px;padding-top:58px">49</div>
  <div class="abs bar" style="left:264px;top:410px;width:35px;height:188px;padding-top:75px">60</div>
  <div class="abs tick" style="left:57px">0°</div>
  <div class="abs tick" style="left:107px">15°</div>
  <div class="abs tick" style="left:158px">30°</div>
  <div class="abs tick" style="left:211px">45°</div>
  <div class="abs tick" style="left:264px">60°</div>
  <div class="abs axis-x">DEGREES OF FORWARD HEAD TILT</div>
  <div class="abs axis-y">PRESSURE ON THE SPINE (LBS)</div>

  <div class="abs figure-art" role="img" aria-label="Illustration of a man walking while looking down at his phone"></div>
  <svg class="abs" style="left:0;top:0" width="763" height="700" aria-hidden="true">
    <g stroke="var(--red)" stroke-width="1">
      <line x1="437" y1="262" x2="529" y2="262"/>
      <line x1="508" y1="294" x2="574" y2="294"/>
      <line x1="510" y1="333" x2="576" y2="333"/>
      <line x1="560" y1="384" x2="590" y2="384"/>
      <line x1="499" y1="445" x2="590" y2="445"/>
      <line x1="566" y1="582" x2="596" y2="582"/>
    </g>
    <g fill="var(--red)" stroke="var(--white)" stroke-width="2">
      <circle cx="437" cy="262" r="6"/>
      <circle cx="508" cy="294" r="6"/>
      <circle cx="510" cy="333" r="6"/>
      <circle cx="560" cy="384" r="6"/>
      <circle cx="499" cy="445" r="6"/>
      <circle cx="566" cy="582" r="6"/>
    </g>
  </svg>
  <div class="abs symptom" style="left:532px;top:237px">HEADACHES</div>
  <div class="abs symptom" style="left:576px;top:280px">NECK PAIN</div>
  <div class="abs symptom" style="left:578px;top:319px">SHOULDER PAIN</div>
  <div class="abs symptom" style="left:594px;top:370px">BACK PAIN</div>
  <div class="abs symptom" style="left:594px;top:430px">ARM AND<br>HAND PAIN</div>
  <div class="abs symptom" style="left:600px;top:568px">SCIATICA</div>

  <div class="abs lower"></div>
  <svg class="abs" style="left:109px;top:704px" width="90" height="90" aria-hidden="true">
    <circle cx="45" cy="45" r="45" fill="var(--navy)"/>
    <path d="M45 45 L45 0 A45 45 0 0 1 74 79 Z" fill="var(--green)"/>
  </svg>
  <div class="abs stat">
    <div class="stat-a">THE AVERAGE PERSONS SPENDS</div>
    <div class="stat-b">8-11 HOURS PER DAY</div>
    <div class="stat-c">USING ELECTRONIC DEVICES</div>
  </div>
  <div class="abs divider"></div>
  <div class="abs care">
    <p><b>CHIROPRACTIC CARE</b> CAN HELP</p>
    <p class="sm">CORRECT AND PREVENT THESE PROBLEMS</p>
    <p>BY <b>RESTORING</b> AND <b>MAINTAINING</b></p>
    <p><b>PROPER ALIGNMENT</b> OF THE <b>NECK,</b></p>
    <p><b>MIDDLE AND LOWER BACK</b></p>
  </div>

  <div class="abs band-green" style="top:893px;height:7px"></div>
  <div class="abs footer"></div>
  <div class="abs portrait" role="img" aria-label="Portrait photo of the chiropractor"></div>
  <div class="abs doc-name">Dr. Samuel Harlow</div>
  <div class="abs doc-addr">Now in Fremantle at 72 Marlow Street</div>
  <div class="abs book">BOOK NOW
    <svg class="phone-icon" viewBox="0 0 28 28" aria-hidden="true">
      <circle cx="14" cy="14" r="14" fill="var(--green)"/>
      <path d="M10 7.5c.6-.4 1.3-.2 1.6.4l1.2 2.4c.3.6.1 1.2-.4 1.6l-.9.6c.7 1.7 1.9 2.9 3.6 3.6l.6-.9c.4-.5 1-.7 1.6-.4l2.4 1.2c.6.3.8 1 .4 1.6l-.9 1.4c-.5.7-1.4 1-2.2.8-4.3-1.2-7.5-4.4-8.7-8.7-.2-.8.1-1.700.8-2.2z" fill="var(--white)"/>
    </svg>
    0400 555 019</div>

  <div class="abs offer">
    <div class="offer-top">
      <span class="offer-pct">50</span>
      <span class="offer-off"><span>%</span><br>OFF</span>
      <span class="offer-head">INITIAL<br>CONSULTATION</span>
    </div>
    <div class="offer-rule"><i></i>If you book online at<i></i></div>
    <div class="offer-url">www.SpineEaseClinic.com.au</div>
    <div class="offer-note">*Choose “<b>TECH NECK</b>” option</div>
  </div>
</div>
</body>
</html>
```